731 Orchard Avenue Residences

designing a sign for apartment complex;
prefer colors gray white and yellow

Target Market(s)

residents coming home to their apartment

Font styles to use
Serif
Sans Serif

Colors
FFF300
FFF600
FEFA6F
FFFEC7
FFFEE8

Requirements
Must have
• black or gray, white and some yellow; easy to read and see

```html
<!DOCTYPE html>
<html lang="en">
<head>
<meta charset="utf-8">
<title>731 Orchard Avenue Residences – Entrance Sign</title>
<link href="https://fonts.googleapis.com/css2?family=Bodoni+Moda:opsz,wght@6..96,400;6..96,700&display=swap" rel="stylesheet">
<style>
  :root {
    --backdrop: #505050;
    --sign-white: #f4f4f4;
    --ink: #000000;
    --accent-yellow: #f2bb0c;
  }
  html, body {
    margin: 0;
    padding: 0;
    width: 1200px;
    height: 1200px;
    overflow: hidden;
    background: var(--backdrop);
  }
  .canvas {
    position: relative;
    width: 1200px;
    height: 1200px;
  }
  .sign {
    position: absolute;
    left: 240px;
    top: 60px;
    width: 720px;
    height: 1080px;
    display: block;
  }
  .sign__panel { fill: var(--sign-white); }
  .sign__band { fill: var(--accent-yellow); }
  .sign__number,
  .sign__street-name,
  .sign__street-type {
    font-family: "Bodoni Moda", "Didot", "Bodoni 72", serif;
    fill: var(--ink);
  }
  .sign__number { font-size: 430px; font-weight: 400; }
  .sign__street-name { font-size: 110px; font-weight: 400; }
  .sign__street-type { font-size: 156px; font-weight: 700; }
</style>
</head>
<body>
  <main class="canvas">
    <svg class="sign" viewBox="0 0 720 1080" role="img" aria-label="731 Orchard Avenue address sign">
      <rect class="sign__panel" x="0" y="0" width="720" height="1080"/>
      <text class="sign__number" x="47" y="409" textLength="623" lengthAdjust="spacingAndGlyphs">731</text>
      <text class="sign__street-name" x="48" y="541" textLength="622" lengthAdjust="spacingAndGlyphs">ORCHARD</text>
      <text class="sign__street-type" x="48" y="696" textLength="631" lengthAdjust="spacingAndGlyphs">AVENUE</text>
      <rect class="sign__band" x="0" y="1055" width="720" height="25"/>
    </svg>
  </main>
</body>
</html>
```